依頼詳細
【チラシデザイン】
添付画像のイメージは、よく見る講座(セミナー)チラシのデザインではなく、映画のポスターのようなイメージ。あまりごちゃごちゃと文字があるより、余白をうまく使ってスッキリしたデザインがいい。キャッチコピーが目に飛び込むような工夫。

※添付ファイルご確認ください(イメージするポスター画像)

【販促詳細】
トピエナにてポスティングを計画しています。
愛知県日進市の中で一番40~45歳女性が多いとデータがあった町1600世帯。

【講座概要】
開催日:4/6(火)10時30分~11時30分 (受付開始10時15分)
受講料:無料  定員:10名  Web(オンライン)講座
申込方法:①電話申込み(お問合せ)0120-493-268
②QRコード(サイト申込み)➡ https://soratsubame-example.or.jp/event-t/30590827452
カリキュラム:
① アラフォー世代の主婦が抱える悩みのタネ
② 長生きリスクの実態とシニアが抱える不安
③ 認知症による想定外の事態~事例紹介~
④ 認知症になる前だったら使えた制度

ミートリンクを利用したオンライン講座 WEB配信 です。
操作に不安な方は、事務局にて事前サポートいたします。

記載項目
キャッチコピー:『大丈夫よ』そんな母の言葉 鵜呑みにしてませんか?
サブキャッチ:子どもに心配をかけたくない、親のウソ
親の言葉に安堵したい、子の現実逃避

受付:そらつばめ事務局  〒530-0099 大阪市北区緑葉町4-2-6-312
TEL:06-6492-3175
主催:そらつばめ(一般社団法人地域交流推進協会)
※広告右下にフォントサイズ6ptで記載➡[文書管理番号 30590827452]

サイズ
A4
ページ数
片面
希望イメージ
シンプル 複雑
単色 カラフル
暗い 明るい
日常 高級
遊び心 厳粛
未来的 伝統的
女性的 男性的
希望する色
緑系、青系、水色系
納品ファイル
補足説明
WEB記事も公開しています。

https://soratsubame-example.or.jp/event-t/30590827452

キャッチ、サブキャッチが見やすく、離れて暮らす母に想いを寄せる女性をうまく表現頂けたことが理由です。また、その後の対応もスピーディーに行なって頂き、最終の完成までストレスなく進めていくことができました。ありがとうございました!

依頼してから1週間の納期で、費用も最小限であったにも関わらず、たくさんのデザイナーの方からご提案を頂くことができ、大変感謝しています。また今後も定期的にイベント開催を予定していきますので、その節はまたよろしくお願いします。どうもありがとうございました!

```html
<!DOCTYPE html>
<html lang="ja">
<head>
<meta charset="UTF-8">
<title>「大丈夫よ」ホントは気になる…離れて暮らす親の健康</title>
<link href="https://fonts.googleapis.com/css2?family=Shippori+Mincho:wght@500;700;800&family=Noto+Sans+JP:wght@400;500;700;900&display=swap" rel="stylesheet">
<style>
  :root{
    --navy:#1d3563;
    --blue:#2b62ad;
    --sky-top:#4f9fe0;
    --sky-mid:#9ccbf0;
    --sky-low:#e3eef8;
    --blossom:#efd9df;
    --ink:#222a36;
    --paper:#ffffff;
    --rule:#2b62ad;
  }
  *{margin:0;padding:0;box-sizing:border-box}
  html,body{width:849px;height:1200px;overflow:hidden;background:var(--paper)}
  .flyer{position:relative;width:849px;height:1200px;overflow:hidden;background:var(--paper);color:var(--ink);font-family:"Noto Sans JP",sans-serif}

  .hero-photo{position:absolute;left:0;top:0;width:849px;height:905px;
    background:linear-gradient(180deg,var(--sky-top) 0%,var(--sky-mid) 45%,var(--sky-low) 72%,var(--blossom) 100%)}

  .vertical{writing-mode:vertical-rl;font-family:"Shippori Mincho",serif;color:var(--navy)}

  .sub-catch{position:absolute;right:70px;top:70px;font-size:23px;font-weight:700;line-height:46px;letter-spacing:3px}
  .sub-catch .gap{display:inline-block;height:0}
  .catch-main{position:absolute;left:88px;top:170px;font-size:118px;font-weight:800;letter-spacing:-2px;line-height:1}
  .catch-lead{position:absolute;left:268px;top:540px;font-size:21px;font-weight:700;line-height:36px;letter-spacing:3px}

  .info{position:absolute;left:0;top:905px;width:849px;height:295px;padding:0 40px}
  .web-row{display:flex;align-items:center;gap:12px;margin-top:8px}
  .web-label{border:2px solid var(--blue);color:var(--blue);font-weight:700;font-size:17px;padding:1px 10px;white-space:nowrap}
  .web-note{font-size:10px;line-height:1.45;color:var(--ink)}
  .headline{font-size:35px;font-weight:900;color:var(--blue);letter-spacing:1px;margin-top:6px;line-height:1.25;border-bottom:2px solid var(--rule);padding-bottom:6px}

  .details{display:flex;align-items:stretch;margin-top:10px;gap:16px;height:88px}
  .curriculum{width:250px;font-size:10px;line-height:1.6}
  .curriculum h3{font-size:11px;font-weight:700;color:var(--blue)}
  .when{display:flex;align-items:baseline;gap:6px;white-space:nowrap}
  .when .tag{font-size:11px;font-weight:700;color:var(--blue)}
  .when .year{font-size:12px}
  .when .date{font-size:46px;font-weight:900;color:var(--navy);line-height:1}
  .when .dow{font-size:17px;font-weight:700;color:var(--navy)}
  .times{font-size:11px;line-height:1.5;white-space:nowrap}
  .fee{display:flex;flex-direction:column;justify-content:center;gap:4px;white-space:nowrap}
  .fee p{font-size:11px}
  .fee strong{font-size:24px;font-weight:900;color:var(--navy);margin-left:4px}
  .apply{flex:1;font-size:10.5px;line-height:1.55;border-left:1px solid var(--rule);padding-left:12px}
  .apply h3{font-size:11px;color:var(--blue)}
  .apply .tel{font-size:19px;font-weight:900;color:var(--navy);display:flex;align-items:center;gap:5px}
  .apply .url{font-size:8.5px;word-break:break-all}

  .footer{margin-top:12px;border-top:1px solid var(--rule);padding-top:7px;font-size:11px;line-height:1.6}
  .footer b{color:var(--blue)}
  .doc-no{position:absolute;right:40px;bottom:52px;font-size:8px;color:var(--ink)}
</style>
</head>
<body>
<main class="flyer">
  <div class="hero-photo" role="img" aria-label="青空の下、満開の桜並木を眺める母と娘の後ろ姿の写真"></div>

  <p class="vertical sub-catch">子どもに心配をかけたくない、<br>親のウソ<br>親の言葉に安堵したい、<br>子の現実逃避</p>
  <h1 class="vertical catch-main">「大丈夫よ」</h1>
  <p class="vertical catch-lead">そんな母の言葉<br>鵜呑みにしてませんか?</p>

  <section class="info">
    <div class="web-row">
      <span class="web-label">Web(オンライン)講座</span>
      <p class="web-note">※ミートリンクを利用したオンライン講座(WEB配信)です。<br>操作に不安な方は、事務局にて事前サポートいたします。</p>
    </div>
    <h2 class="headline">ホントは気になる…離れて暮らす親の健康</h2>

    <div class="details">
      <div class="curriculum">
        <h3>【カリキュラム】</h3>
        <p>① アラフォー世代の主婦が抱える悩みのタネ<br>② 長生きリスクの実態とシニアが抱える不安<br>③ 認知症による想定外の事態~事例紹介~<br>④ 認知症になる前だったら使えた制度</p>
      </div>
      <div>
        <div class="when"><span class="tag">開催日</span><span class="year">2021</span><span class="date">4/6</span><span class="dow">(火)</span></div>
        <p class="times">10時30分~11時30分<br>(受付開始10時15分)</p>
      </div>
      <div class="fee">
        <p>受講料<strong>無料</strong></p>
        <p>定員<strong>10名</strong></p>
      </div>
      <div class="apply">
        <h3>【申込方法】</h3>
        <p>①電話申込み(お問合せ)</p>
        <p class="tel"><svg width="16" height="16" viewBox="0 0 24 24" aria-hidden="true"><path fill="#1d3563" d="M6.6 10.8a15.1 15.1 0 0 0 6.6 6.6l2.2-2.2a1 1 0 0 1 1-.25 11.4 11.4 0 0 0 3.6.57 1 1 0 0 1 1 1V20a1 1 0 0 1-1 1A17 17 0 0 1 3 4a1 1 0 0 1 1-1h3.5a1 1 0 0 1 1 1c0 1.25.2 2.45.57 3.57a1 1 0 0 1-.25 1z"/></svg>0120-493-268</p>
        <p>②サイト申込み</p>
        <p class="url">https://soratsubame-example.or.jp/event-t/30590827452</p>
      </div>
    </div>

    <div class="footer">
      <p><b>【受付】</b>そらつばめ事務局 〒530-0099 大阪市北区緑葉町4-2-6-312 TEL 06-6492-3175</p>
      <p><b>【主催】</b>そらつばめ(一般社団法人地域交流推進協会)</p>
    </div>
  </section>
  <p class="doc-no">文書管理番号 30590827452</p>
</main>
</body>
</html>
```